you will use Ai to Copy the website Wanderbay.com to come up with the basic frame work and it will give you the understanding of how I would like Coachlend.com to be like. Coachlend.com is a peer to peer rv rental site very similar to both of the other rv rental sites the difference is that are commission based 20% and above per rental and we will be one flat monthly rate and they keep all the earnings. Below is photo that will help you with the color scheme and the look and feel of the design

1 page

```html
<!DOCTYPE html>
<html lang="en">
<head>
<meta charset="utf-8">
<title>Coachlend – Peer to Peer RV Rental</title>
<link href="https://fonts.googleapis.com/css2?family=Manrope:wght@400;500;600;700;800&display=swap" rel="stylesheet">
<style>
:root{
  --green:#5a9a2c;
  --green-dark:#4b8424;
  --ink:#1f2a33;
  --body:#3d4650;
  --muted:#7a828a;
  --line:#dfe2e5;
  --sand:#f4f3ee;
  --lime:#d9e7bd;
  --night:#1d252d;
  --white:#ffffff;
}
*{box-sizing:border-box;margin:0;padding:0}
html,body{width:1200px;height:3953px;overflow:hidden}
body{position:relative;font-family:'Manrope',sans-serif;color:var(--ink);background:var(--white)}
.abs{position:absolute}
.btn{position:absolute;display:flex;align-items:center;justify-content:center;border-radius:999px;font-weight:600;font-size:14px}
.btn-green{background:var(--green);color:var(--white)}
.btn-outline{border:1.5px solid var(--ink);color:var(--ink);background:var(--white)}
.btn-dark{background:var(--night);color:var(--white)}

/* Hero */
.hero{left:0;top:0;width:1200px;height:660px;overflow:hidden}
.hero-photo{position:absolute;inset:0;background:linear-gradient(180deg,#d8cdd6 0%,#c6ccd6 22%,#aeb8bf 38%,#7d8c84 52%,#4f5f4a 68%,#3c4a36 82%,#5a5a4a 100%)}
.hero-curve{position:absolute;left:0;bottom:0}
.brand{position:absolute;left:107px;top:0;width:95px;height:80px;background:var(--night);display:flex;align-items:center;justify-content:center;color:var(--white);font-weight:700;font-size:11px;border-radius:0 0 4px 4px}
.nav a{position:absolute;top:32px;font-size:12.5px;color:var(--ink);text-decoration:none}
.nav a.active{color:var(--green)}
.signin{left:873px;top:22px;width:88px;height:36px;border:1.5px solid var(--ink);color:var(--ink)}
.getstarted{left:991px;top:22px;width:100px;height:36px;font-size:13.5px}
.hero h1{position:absolute;left:0;width:1200px;text-align:center;font-size:46px;font-weight:700;letter-spacing:-.5px;line-height:1}
.hero .l1{top:120px;color:var(--ink)}
.hero .l2{top:184px;color:var(--green)}
.hero .sub{position:absolute;top:246px;width:1200px;text-align:center;font-size:18px;color:var(--ink)}

.search{left:107px;top:622px;width:984px;height:73px;background:var(--white);border-radius:40px;box-shadow:0 6px 18px rgba(0,0,0,.14)}
.field{position:absolute;top:0;height:73px;display:flex;align-items:center;gap:12px;font-size:14px;color:var(--ink)}
.ico{width:32px;height:32px;border-radius:50%;background:#e4eed6;display:flex;align-items:center;justify-content:center}
.field small{display:block;font-size:11.5px;color:var(--muted)}
.sep{position:absolute;top:22px;width:1px;height:30px;background:var(--line)}
.search .go{left:826px;top:16px;width:128px;height:40px}

/* Income */
.income-photo{left:163px;top:780px;width:343px;height:348px;border-radius:18px;background:linear-gradient(180deg,#e9b06a 0%,#d98f4a 30%,#7f8a55 60%,#3f5a33 100%)}
.income h2{position:absolute;left:570px;font-size:38px;font-weight:700;letter-spacing:-.5px}
.income .h-a{top:798px;color:var(--ink)}
.income .h-b{top:850px;color:var(--green)}
.income p{position:absolute;left:570px;width:480px;font-size:11.5px;line-height:20px;color:var(--body)}
.income .b1{left:570px;top:1076px;width:142px;height:36px;font-size:13.5px}
.income .b2{left:738px;top:1076px;width:245px;height:36px;font-size:13.5px}

/* Find */
.find{left:0;top:1217px;width:1200px;height:1098px;background:var(--sand)}
.find h2{position:absolute;top:88px;width:1200px;text-align:center;font-size:38px;font-weight:700;letter-spacing:-.5px}
.tabs span{position:absolute;top:182px;font-size:13.5px;font-weight:500;color:var(--ink)}
.tabs span.on{color:var(--green)}
.tabs i{position:absolute;left:158px;top:209px;width:82px;height:2px;background:var(--green)}
.card{position:absolute;width:317px;height:327px;background:var(--white);border-radius:6px;overflow:hidden}
.card .ph{height:169px}
.card .heart{position:absolute;left:14px;top:12px;width:24px;height:24px;border-radius:50%;background:var(--white);display:flex;align-items:center;justify-content:center}
.card .tag{position:absolute;left:12px;top:138px;padding:4px 9px;background:rgba(255,255,255,.85);border-radius:4px;font-size:11px;color:var(--body)}
.card h3{position:absolute;left:12px;top:190px;font-size:13.5px;font-weight:500}
.card .rate{position:absolute;left:12px;top:222px;font-size:11px;color:var(--body)}
.card .rate b{color:var(--green)}
.card .cls{position:absolute;left:12px;top:251px;font-size:11px;color:var(--body)}
.card .price{position:absolute;left:12px;top:279px;height:30px;padding:0 9px;background:var(--green);color:var(--white);font-size:13.5px;font-weight:600;border-radius:4px;display:flex;align-items:center}
.more{left:530px;top:979px;width:141px;height:35px;font-size:13px}

/* Better */
.better h2{position:absolute;width:1200px;text-align:center;font-size:38px;font-weight:700;letter-spacing:-.5px;line-height:1}
.feat{position:absolute;top:2533px;width:290px}
.feat .box{position:absolute;left:0;top:0;width:56px;height:56px;background:var(--night);border-radius:3px;display:flex;align-items:center;justify-content:center}
.feat h4{position:absolute;left:70px;top:0;font-size:14.5px;font-weight:700;line-height:18px;width:220px}
.feat p{position:absolute;left:70px;top:44px;width:215px;font-size:11px;line-height:18px;color:var(--muted)}
.vline{position:absolute;top:2532px;width:1px;height:100px;background:var(--line)}

/* Testimonials */
.testi{left:0;top:2709px;width:1200px;height:530px;background:var(--lime);overflow:hidden}
.testi .eyebrow{position:absolute;top:74px;width:1200px;text-align:center;font-size:13px;color:var(--green)}
.testi h2{position:absolute;top:104px;width:1200px;text-align:center;font-size:38px;font-weight:700;letter-spacing:-.5px}
.tcard{position:absolute;top:200px;width:330px;height:190px;background:var(--white);border-radius:4px}
.tcard .st{position:absolute;left:25px;top:18px;font-size:11.5px;font-weight:700}
.tcard .st b{color:var(--green);letter-spacing:2px;font-weight:600}
.tcard q{position:absolute;left:25px;top:50px;width:290px;font-size:11px;line-height:18px;color:var(--body)}
.tcard .av{position:absolute;left:25px;top:126px;width:48px;height:48px;border-radius:50%;background:linear-gradient(180deg,#8b8f93,#4a4f54)}
.tcard .who{position:absolute;left:83px;top:142px;font-size:13px;font-weight:600}
.arrow{position:absolute;top:425px;width:41px;height:41px;border-radius:50%;display:flex;align-items:center;justify-content:center}

/* CTA */
.cta{left:0;top:3239px;width:1200px;height:353px;overflow:hidden}
.cta-photo{position:absolute;inset:0;background:linear-gradient(120deg,#1c2530 0%,#2e3a44 40%,#6b5a3e 62%,#3a4046 80%,#1f272e 100%)}
.cta h2{position:absolute;top:100px;width:1200px;text-align:center;color:var(--white);font-size:38px;font-weight:700}
.cta p{position:absolute;top:158px;width:1200px;text-align:center;color:#e7eaec;font-size:15px;line-height:23px}
.cta .b1{left:454px;top:233px;width:142px;height:36px}
.cta .b2{left:606px;top:233px;width:137px;height:36px;border:1.5px solid var(--white);color:var(--white)}

/* Footer */
.f-logo{left:112px;top:3688px;width:144px;height:145px;background:var(--night);display:flex;align-items:center;justify-content:center;color:var(--white);font-weight:700;font-size:17px}
.f-title{position:absolute;top:3663px;font-size:15px;font-weight:500;color:var(--green)}
.f-link{position:absolute;font-size:11.5px;color:var(--ink)}
.f-row{position:absolute;left:619px;display:flex;align-items:center;gap:14px;font-size:11.5px}
.f-row .ico{width:30px;height:30px}
.soc{position:absolute;top:3714px;width:33px;height:33px;border:1.5px solid var(--ink);border-radius:50%}
.bar{left:0;top:3911px;width:1200px;height:42px;background:var(--night);color:#d8dcdf;font-size:11px;display:flex;align-items:center;justify-content:center}
</style>
</head>
<body>

<section class="hero abs">
  <div class="hero-photo" role="img" aria-label="Motorhome parked at a forest campsite below snowy mountains, travellers gathered around a campfire"></div>
  <svg class="hero-curve" width="1200" height="60" viewBox="0 0 1200 60"><path d="M0 0 Q600 40 1200 0 L1200 60 L0 60 Z" fill="#ffffff"/></svg>
  <div class="brand">Coachlend.com</div>
  <nav class="nav">
    <a class="active" style="left:378px">Home</a>
    <a style="left:461px">About</a>
    <a style="left:546px">Browse RVs</a>
    <a style="left:660px">List Your RV</a>
    <a style="left:774px">How It Works</a>
  </nav>
  <div class="btn signin">Sign In</div>
  <div class="btn btn-green getstarted">Get Started</div>
  <h1 class="l1">YOUR NEXT ADVENTURE</h1>
  <h1 class="l2">STARTS HERE</h1>
  <div class="sub">Find the perfect RV for your next road trip.</div>
</section>

<div class="search abs">
  <div class="field" style="left:31px">
    <span class="ico"><svg width="16" height="16" viewBox="0 0 24 24" fill="none" stroke="#5a9a2c" stroke-width="2"><path d="M12 22s7-7 7-12a7 7 0 0 0-14 0c0 5 7 12 7 12z"/><circle cx="12" cy="10" r="2.5"/></svg></span>
    <span>Where?<small>Search Location</small></span>
  </div>
  <div class="sep" style="left:190px"></div>
  <div class="field" style="left:242px">
    <span class="ico"><svg width="16" height="16" viewBox="0 0 24 24" fill="none" stroke="#3d4650" stroke-width="2"><rect x="4" y="5" width="16" height="15" rx="2"/><path d="M4 10h16M9 3v4M15 3v4"/></svg></span>
    <span>Pick-up Date</span>
  </div>
  <div class="sep" style="left:410px"></div>
  <div class="field" style="left:452px">
    <span class="ico"><svg width="16" height="16" viewBox="0 0 24 24" fill="none" stroke="#3d4650" stroke-width="2"><rect x="4" y="5" width="16" height="15" rx="2"/><path d="M4 10h16M9 3v4M15 3v4"/></svg></span>
    <span>Return Date</span>
  </div>
  <div class="sep" style="left:660px"></div>
  <div class="field" style="left:660px;left:661px;padding-left:8px">
    <span class="ico"><svg width="16" height="16" viewBox="0 0 24 24" fill="none" stroke="#3d4650" stroke-width="2"><circle cx="12" cy="8" r="4"/><path d="M4 21c1-4 4-6 8-6s7 2 8 6"/></svg></span>
    <span>Passenger</span>
    <svg width="12" height="12" viewBox="0 0 24 24" fill="none" stroke="#1f2a33" stroke-width="2.5"><path d="M6 9l6 6 6-6"/></svg>
  </div>
  <div class="btn btn-green go">Search&nbsp;&nbsp;<svg width="14" height="14" viewBox="0 0 24 24" fill="none" stroke="#fff" stroke-width="2.5"><circle cx="11" cy="11" r="7"/><path d="M20 20l-4-4"/></svg></div>
</div>

<section class="income">
  <div class="income-photo abs" role="img" aria-label="Couple standing beside a camper van on a mountain road at sunset"></div>
  <h2 class="h-a">Your RV. Your Income.</h2>
  <h2 class="h-b">Your Way.</h2>
  <p style="top:926px">Your RV doesn't have to sit in the driveway when you're not using it.<br>Coachlend makes it simple to share your RV with travelers and earn money from an asset you already own.<br>And unlike commission-based rental platforms, Coachlend doesn't take a percentage of every rental.<br>Pay one simple monthly membership and keep your rental earnings.</p>
  <div class="btn btn-green b1">List Your RV</div>
  <div class="btn btn-outline b2">See How Much You Could Earn</div>
</section>

<section class="find abs">
  <h2>Find Your Perfect RV</h2>
  <div class="tabs">
    <span class="on" style="left:158px">Motorhomes</span>
    <span style="left:312px">Camper Vans</span>
    <span style="left:470px">Travel Trailers</span>
    <span style="left:631px">Fifth Wheels</span>
    <span style="left:783px">Toy Haulers</span>
    <span style="left:930px">Pop-Up Campers</span>
    <i></i>
  </div>

  <div class="card" style="left:107px;top:252px">
    <div class="ph" role="img" aria-label="White motorhome parked among green trees" style="background:linear-gradient(180deg,#8fae6e,#4f7040)"></div>
    <span class="heart"><svg width="12" height="12" viewBox="0 0 24 24" fill="none" stroke="#1f2a33" stroke-width="2"><path d="M12 20s-8-5-8-11a4.5 4.5 0 0 1 8-2.5A4.5 4.5 0 0 1 20 9c0 6-8 11-8 11z"/></svg></span>
    <span class="tag">Highly Rated</span>
    <h3>2024 Ridgeline Voyager</h3><div class="rate"><b>★</b> 4.9 · 24 reviews</div><div class="cls">Class C · Sleeps 6</div><div class="price">$189 / night</div>
  </div>
  <div class="card" style="left:442px;top:252px">
    <div class="ph" role="img" aria-label="White motorhome under a blue sky" style="background:linear-gradient(180deg,#a9c3dc,#dfe3e6 70%,#8a9a7a)"></div>
    <span class="heart"><svg width="12" height="12" viewBox="0 0 24 24" fill="none" stroke="#1f2a33" stroke-width="2"><path d="M12 20s-8-5-8-11a4.5 4.5 0 0 1 8-2.5A4.5 4.5 0 0 1 20 9c0 6-8 11-8 11z"/></svg></span>
    <span class="tag">Highly Rated</span>
    <h3>2024 Ridgeline Voyager</h3><div class="rate"><b>★</b> 4.9 · 24 reviews</div><div class="cls">Class C · Sleeps 6</div><div class="price">$189 / night</div>
  </div>
  <div class="card" style="left:775px;top:252px">
    <div class="ph" role="img" aria-label="Motorhome parked on a rocky coastal hillside" style="background:linear-gradient(180deg,#b8c6d2,#8a9a80 55%,#6a7a5a)"></div>
    <span class="heart"><svg width="12" height="12" viewBox="0 0 24 24" fill="none" stroke="#1f2a33" stroke-width="2"><path d="M12 20s-8-5-8-11a4.5 4.5 0 0 1 8-2.5A4.5 4.5 0 0 1 20 9c0 6-8 11-8 11z"/></svg></span>
    <span class="tag">Highly Rated</span>
    <h3>2024 Ridgeline Voyager</h3><div class="rate"><b>★</b> 4.9 · 24 reviews</div><div class="cls">Class C · Sleeps 6</div><div class="price">$189 / night</div>
  </div>
  <div class="card" style="left:107px;top:602px">
    <div class="ph" role="img" aria-label="Green camper van with open doors in a forest" style="background:linear-gradient(180deg,#3f5a38,#5d6f45 60%,#6a6a4a)"></div>
    <span class="heart"><svg width="12" height="12" viewBox="0 0 24 24" fill="none" stroke="#1f2a33" stroke-width="2"><path d="M12 20s-8-5-8-11a4.5 4.5 0 0 1 8-2.5A4.5 4.5 0 0 1 20 9c0 6-8 11-8 11z"/></svg></span>
    <span class="tag">Highly Rated</span>
    <h3>2024 Ridgeline Voyager</h3><div class="rate"><b>★</b> 4.9 · 24 reviews</div><div class="cls">Class C · Sleeps 6</div><div class="price">$189 / night</div>
  </div>
  <div class="card" style="left:442px;top:602px">
    <div class="ph" role="img" aria-label="Classic white camper van parked on a street" style="background:linear-gradient(180deg,#6c7a86,#cfd2d0 50%,#5d6468)"></div>
    <span class="heart"><svg width="12" height="12" viewBox="0 0 24 24" fill="none" stroke="#1f2a33" stroke-width="2"><path d="M12 20s-8-5-8-11a4.5 4.5 0 0 1 8-2.5A4.5 4.5 0 0 1 20 9c0 6-8 11-8 11z"/></svg></span>
    <span class="tag">Highly Rated</span>
    <h3>2024 Ridgeline Voyager</h3><div class="rate"><b>★</b> 4.9 · 24 reviews</div><div class="cls">Class C · Sleeps 6</div><div class="price">$189 / night</div>
  </div>
  <div class="card" style="left:775px;top:602px">
    <div class="ph" role="img" aria-label="Traveller beside a camper van below red canyon cliffs" style="background:linear-gradient(180deg,#9a6248,#b57a58 50%,#d8d4cc)"></div>
    <span class="heart"><svg width="12" height="12" viewBox="0 0 24 24" fill="none" stroke="#1f2a33" stroke-width="2"><path d="M12 20s-8-5-8-11a4.5 4.5 0 0 1 8-2.5A4.5 4.5 0 0 1 20 9c0 6-8 11-8 11z"/></svg></span>
    <span class="tag">Highly Rated</span>
    <h3>2024 Ridgeline Voyager</h3><div class="rate"><b>★</b> 4.9 · 24 reviews</div><div class="cls">Class C · Sleeps 6</div><div class="price">$189 / night</div>
  </div>
  <div class="btn btn-dark more">Show More</div>
</section>

<section class="better">
  <h2 style="top:2390px;color:var(--ink)">A Better Way to Rent</h2>
  <h2 style="top:2442px;color:var(--green)">Your RV</h2>

  <div class="feat" style="left:112px">
    <div class="box"><svg width="30" height="30" viewBox="0 0 24 24" fill="none" stroke="#fff" stroke-width="1.6"><ellipse cx="15" cy="6" rx="5" ry="2"/><path d="M10 6v4c0 1.1 2.2 2 5 2s5-.9 5-2V6M10 10v4c0 1.1 2.2 2 5 2s5-.9 5-2v-4"/><circle cx="8" cy="16" r="4.5"/></svg></div>
    <h4>Keep More<br>No Commission</h4>
    <p>You pay a simple monthly membership instead of giving up a percentage of every booking.</p>
  </div>
  <div class="vline" style="left:425px"></div>
  <div class="feat" style="left:465px">
    <div class="box"><svg width="30" height="30" viewBox="0 0 24 24" fill="none" stroke="#fff" stroke-width="1.6"><rect x="5" y="4" width="14" height="14" rx="2"/><path d="M5 11h14M7 18v2M17 18v2"/><circle cx="8.5" cy="14.5" r="1"/><circle cx="15.5" cy="14.5" r="1"/></svg></div>
    <h4>Your RV<br>Your Rules</h4>
    <p>Create your listing, set your availability, establish your pricing and decide when you want to rent.</p>
  </div>
  <div class="vline" style="left:777px"></div>
  <div class="feat" style="left:818px">
    <div class="box"><svg width="28" height="28" viewBox="0 0 24 24" fill="#fff"><path d="M13 2L5 14h6l-1 8 8-12h-6z"/></svg></div>
    <h4>Simple &amp;<br>Straightforward</h4>
    <p>A clean platform designed to make listing, discovering and booking RVs easier.</p>
  </div>
</section>

<section class="testi abs">
  <div class="eyebrow">Testimonial</div>
  <h2>Rv Owners Love Coachlend</h2>
  <div class="tcard" style="left:-84px"><div class="st">5.0 <b>★★★★★</b></div><q>Coachlend gives us a simple way to offset the cost of owning our RV without giving away a percentage of every rental.</q><div class="av"></div><div class="who">RV Owner</div></div>
  <div class="tcard" style="left:262px"><div class="st">5.0 <b>★★★★★</b></div><q>Coachlend gives us a simple way to offset the cost of owning our RV without giving away a percentage of every rental.</q><div class="av"></div><div class="who">RV Owner</div></div>
  <div class="tcard" style="left:607px"><div class="st">5.0 <b>★★★★★</b></div><q>Coachlend gives us a simple way to offset the cost of owning our RV without giving away a percentage of every rental.</q><div class="av"></div><div class="who">RV Owner</div></div>
  <div class="tcard" style="left:952px"><div class="st">5.0 <b>★★★★★</b></div><q>Coachlend gives us a simple way to offset the cost of owning our RV without giving away a percentage of every rental.</q><div class="av"></div><div class="who">RV Owner</div></div>
  <div class="arrow" style="left:551px;background:#fff"><svg width="16" height="16" viewBox="0 0 24 24" fill="none" stroke="#1f2a33" stroke-width="2.5"><path d="M19 12H5M11 6l-6 6 6 6"/></svg></div>
  <div class="arrow" style="left:608px;background:var(--green)"><svg width="16" height="16" viewBox="0 0 24 24" fill="none" stroke="#fff" stroke-width="2.5"><path d="M5 12h14M13 6l6 6-6 6"/></svg></div>
</section>

<section class="cta abs">
  <div class="cta-photo" role="img" aria-label="Travel trailer with a lit awning at a campsite at dusk"></div>
  <h2>Where Will Your RV Take You?</h2>
  <p>Whether you're planning your next adventure or ready to earn from your RV,<br>Coachlend makes getting started simple.</p>
  <div class="btn btn-green b1">Find an RV</div>
  <div class="btn b2">List Your RV</div>
</section>

<footer>
  <div class="f-logo abs">Coachlend.com</div>
  <div class="f-title" style="left:378px">Company</div>
  <div class="f-link" style="left:377px;top:3707px">Home</div>
  <div class="f-link" style="left:377px;top:3741px">About</div>
  <div class="f-link" style="left:380px;top:3775px">Browse RVs</div>
  <div class="f-link" style="left:380px;top:3809px">List Your RV</div>
  <div class="f-link" style="left:377px;top:3843px">How It Works</div>

  <div class="f-title" style="left:619px">Contact Us</div>
  <div class="f-row" style="top:3700px"><span class="ico"><svg width="15" height="15" viewBox="0 0 24 24" fill="none" stroke="#1f2a33" stroke-width="2"><path d="M5 4h4l2 5-2.5 1.5a11 11 0 0 0 5 5L15 13l5 2v4a2 2 0 0 1-2 2A16 16 0 0 1 3 6a2 2 0 0 1 2-2z"/></svg></span>1234567890</div>
  <div class="f-row" style="top:3750px"><span class="ico"><svg width="15" height="15" viewBox="0 0 24 24" fill="none" stroke="#1f2a33" stroke-width="2"><rect x="3" y="5" width="18" height="14" rx="2"/><path d="M3 7l9 6 9-6"/></svg></span>hello@coachlend.com</div>
  <div class="f-row" style="top:3800px"><span class="ico"><svg width="15" height="15" viewBox="0 0 24 24" fill="none" stroke="#1f2a33" stroke-width="2"><path d="M12 22s7-7 7-12a7 7 0 0 0-14 0c0 5 7 12 7 12z"/><circle cx="12" cy="10" r="2.5"/></svg></span>23 house no demo Uk.</div>

  <div class="f-title" style="left:950px">Follow Us</div>
  <div class="soc" style="left:951px"></div>
  <div class="soc" style="left:1004px"></div>
  <div class="soc" style="left:1058px"></div>

  <div class="bar abs">© 2026 Coachlend. All rights reserved. Privacy Policy | Terms of Service</div>
</footer>

</body>
</html>
```